We need a design for our website called Trocadim which is a brazilian e-commerce focused on childrenswear. Basically your are able to swap (sell & buy) your kids outgrown clothes in the website and we will offer all the necessary services to help you on that.

We believe the main characteristic of the company is the swap of clothes and accessories, but we also feel that by doing this we are guaranteeing that this clothes are not going to trash, reducing clothes waste and being friendly with the environment.

We believe it should be clean with solid and soft colors (refer to the logo attached) and should communicate high quality standards and trust.

We need 2 web pages: home/search results and product details. In both pages we would like to have a fixed top bar with the logo, menu (Buy, Sell, About Us), login, a short message and shopping cart. As well as a footer on the botton with different options and social network links.

- Home/search results: right at the beginning of the page we would like to have a welcome/explanatory carousel banner. It should be a conventional 2 columns design with filters on the left (~25%) and the results on the main section (~3/4 products per row). We need filters for clothes and accessories (size,category, brands, color, gender).

- Product details: again, this should be very clean, with breadcrumbs on the top, a very short description (product's name, category, size), price, "Add to cart" button, an image with zoom functionality (as reference: brisk lupex), a "Similar Items" box and a share bar (chatterbook, tweeplr, boardlyx, k+).

Please bear in mind that we plan to use the main template in different colors across the website.
Updates

Hi everyone! 

We have just updated the brief to add some "Must have features" and "Nice to have features". Please take a careful look at it as it affects pretty much every design we received so far.

We will guarantee the project in the next 1-2 days, but we first would like to see some initial proposals for the second page (product details). Some of you guys are doing an awesome job in the home page!

Best,

Trocadim team

We have just updated the contest payment status: it is now committed!

Best,
Trocadim Team

Target Market(s)

The main audience will be parents of any age

Industry/Entity Type

E-Commerce

Requirements
Must have
• We would like to have only the following elements in the header: logo, login, cart image, Home, "Compre" (Buy), "Venda" (Sell) - not necessarily in this order
- The header should be persistent all over the website (always fixed at the top), thus, if it is too thick it will end up eating too much vertical space in some pages
- The current page should be somehow highlited in the header
- Right next to the cart image on the top we need a small tag indicating how many itens are already inside the cart
- We need a button "Entenda como funcionamos" (which in english means "Learn more") in the banner
- Please use an image of childrens in the banner (not clothes or teenagers)
- Besides the banner, the user in a1024x768 screen resolution should at least be able to view the first row of search results
- There is no need for a "Add to cart" button in every search result (keep price, size, type only). This option should only be available in the second page (product details)
- When needed use "Adicionar ao carrinho" (portuguese) instead of "Add to cart" (english)
- Regarding social network links in the footer, we only need chatterbook, tweeplr, boardlyx, k+
- In the search results page we need an option to show 12, 24, 48 results per page
- Users need to be able to sort the results (newest first, price low-high and high-low)
Nice to have
• We don´t need a text search box anywhere in the website
- There is no need to present the payment methods in neither pages
- The image of the cart should be modified when there are items inside (full vs empty)
- When the user moves the mouse over the cart image, a simple "div" should show up bellow it listing all items
- Regarding social network links, we like icons that change colors when the user
moves the mouse over them
- Regarding the color scheme, use up to a max of 3 colors and feel free to change the logo colors if you find a better combination than the ones we provided

```html
<!DOCTYPE html>
<html lang="pt-BR">
<head>
<meta charset="utf-8">
<title>Trocadim – Girls Flower</title>
<link href="https://fonts.googleapis.com/css2?family=Ubuntu:wght@400;500&display=swap" rel="stylesheet">
<style>
:root{
  --lavender:#8f93cf;
  --lavender-dark:#7f84c4;
  --green:#2bb673;
  --cream:#fffdf0;
  --white:#ffffff;
  --text:#555555;
  --muted:#777777;
  --orange:#f0a030;
  --footer-top:#e4e3dc;
  --footer-bottom:#f3f2ec;
}
*{margin:0;padding:0;box-sizing:border-box}
html,body{width:991px;height:1200px;overflow:hidden}
body{position:relative;background:var(--cream);font-family:"Ubuntu",sans-serif;color:var(--text)}
.abs{position:absolute}

.topbar{left:0;top:0;width:991px;height:76px;background:var(--lavender)}
.nav a{position:absolute;top:34px;color:var(--white);font-size:13.5px;text-decoration:none}
.nav .current{font-weight:500}
.brand-box{left:373px;top:0;width:251px;height:88px;background:linear-gradient(#ffffff,#efefef);box-shadow:0 2px 4px rgba(0,0,0,.25);display:flex;align-items:center;justify-content:center}
.brand-box span{color:var(--green);font-size:44px;font-weight:400;letter-spacing:.5px}
.account{left:726px;top:36px;color:var(--white);font-size:11px}
.cart-icon{left:806px;top:28px}
.cart-label{left:834px;top:37px;color:var(--white);font-size:10.5px}

.crumbbar{left:124px;top:118px;width:742px;height:42px;background:var(--white)}
.crumbbar h2{position:absolute;left:16px;top:12px;font-size:16px;font-weight:500;color:var(--lavender)}
.crumbs{position:absolute;right:15px;top:15px;font-size:10.5px;color:var(--text)}
.crumbs .here{color:var(--green)}

.panel{left:124px;top:175px;width:742px;height:658px;background:var(--white)}
.title{left:140px;top:206px;font-size:20.5px;font-weight:500;color:var(--lavender)}
.thumb{width:111px;height:104px}
.thumb-a{left:141px;top:254px;background:linear-gradient(#d9dcdc,#c7cbcb)}
.thumb-b{left:141px;top:377px;background:linear-gradient(#e0e2e2,#cfd2d4)}
.hero{left:268px;top:254px;width:300px;height:326px;background:radial-gradient(circle at 55% 45%,#e9ebeb,#c9cccd)}
.lens{left:389px;top:441px;width:53px;height:53px;background:rgba(255,255,255,.55)}

.specs{left:592px;top:252px;font-size:10.5px;color:var(--text)}
.spec{position:absolute;left:0;white-space:nowrap}
.spec b{font-weight:400;color:var(--green);font-size:12.5px;margin-left:8px}
.spec .price{font-size:16px;font-weight:500}
.spec s{color:var(--text)}
.btn{position:absolute;left:593px;width:161px;height:31px;border-radius:3px;color:var(--white);font-size:12px;display:flex;align-items:center;gap:10px;padding-left:12px}
.btn-cart{top:435px;background:var(--green)}
.btn-fav{top:475px;background:var(--lavender);padding-left:10px}

.related-title{left:141px;top:622px;font-size:15.5px;font-weight:500;color:var(--green)}
.item{position:absolute;top:663px;width:111px}
.item .pic{height:105px}
.item p{margin-top:14px;font-size:11px;color:var(--muted)}

.footer{left:0;top:980px;width:991px;height:220px;background:linear-gradient(var(--footer-top),var(--footer-bottom))}
.foot-brand{left:123px;top:1004px;font-size:24px;color:var(--lavender)}
.foot-contact{left:128px;top:1041px;font-size:9.5px;line-height:19px;color:var(--text)}
.foot-contact span{display:inline-block;width:28px}
.foot-col{top:1009px;font-size:12px;color:var(--orange)}
.foot-col ul{list-style:none;margin-top:17px;font-size:9.5px;line-height:19px;color:var(--muted)}
.cards{left:318px;top:1118px;display:flex;gap:2px}
.cards i{display:block;width:25px;height:15px;border-radius:2px}
.social{left:687px;top:1044px;display:flex;gap:8px}
.social i{display:block;width:27px;height:27px}
</style>
</head>
<body>

<header class="abs topbar">
  <nav class="nav">
    <a class="current" style="left:122px">Home</a>
    <a style="left:194px">Compre</a>
    <a style="left:277px">Venda</a>
  </nav>
</header>
<div class="abs brand-box"><span>Trocadim</span></div>
<div class="abs account">My Account</div>
<svg class="abs cart-icon" width="24" height="22" viewBox="0 0 24 22" fill="none" stroke="#fff" stroke-width="1.6">
  <path d="M1 2h4l3 12h12l3-9H6"/><circle cx="10" cy="18" r="1.6"/><circle cx="18" cy="18" r="1.6"/>
</svg>
<div class="abs cart-label">Cart (3)</div>

<section class="abs crumbbar">
  <h2>CLOTHES</h2>
  <div class="crumbs">Home &gt; Girls <span class="here">&gt; Girls Flower</span></div>
</section>

<main class="abs panel"></main>
<h1 class="abs title">GIRLS FLOWER</h1>
<div class="abs thumb thumb-a" role="img" aria-label="Product photo: legs in striped tights and teal ruffled skirt"></div>
<div class="abs thumb thumb-b" role="img" aria-label="Product photo: girl in lavender top and teal ruffled skirt"></div>
<div class="abs hero" role="img" aria-label="Large product photo: girl jumping in lavender sweater and teal ruffled skirt"></div>
<div class="abs lens">
  <svg width="53" height="53" viewBox="0 0 53 53"><path d="M26.5 18v18M17.5 27h18" stroke="#111" stroke-width="2.4"/></svg>
</div>

<div class="abs specs">
  <div class="spec" style="top:2px">Price : <b>Sale <span class="price">$47.60</span></b>&nbsp;&nbsp;&nbsp;&nbsp;List Price : <s>$68.00</s></div>
  <div class="spec" style="top:38px">Brand : <b style="color:#f08a1c;font-weight:500;font-size:14px">plumkit</b></div>
  <div class="spec" style="top:72px">Type of cloth : <b>Sweater</b></div>
  <div class="spec" style="top:106px">Size : <b>4 XS</b></div>
  <div class="spec" style="top:140px">Condition : <b>New</b></div>
</div>
<div class="btn btn-cart">
  <svg width="16" height="13" viewBox="0 0 16 13" fill="none" stroke="#fff" stroke-width="1.3"><path d="M1 1h3l2 7h7l2-5H5"/><circle cx="7" cy="11" r="1"/><circle cx="12" cy="11" r="1"/></svg>
  Adicionar ao carrinho
</div>
<div class="btn btn-fav">
  <svg width="14" height="14" viewBox="0 0 14 14" fill="none" stroke="#fff" stroke-width="1.3"><rect x="1" y="5" width="12" height="3"/><rect x="2" y="8" width="10" height="5"/><path d="M7 5v8M7 5C5 1 2 2 4 5M7 5c2-4 5-3 3 0"/></svg>
  Adicionar aos favoritos
</div>

<h3 class="abs related-title">RELATED PRODUCTS</h3>
<div class="item" style="left:141px"><div class="pic" role="img" aria-label="Girl in purple ruffled dress" style="background:linear-gradient(#fafafa,#d8c3b8)"></div><p>Lavender Rose</p></div>
<div class="item" style="left:262px"><div class="pic" role="img" aria-label="Girl in teal top" style="background:linear-gradient(#f2f2f2,#8fd1c4)"></div><p>Lavender Rose</p></div>
<div class="item" style="left:382px"><div class="pic" role="img" aria-label="Girl in pink dress" style="background:linear-gradient(#e8e6e2,#f0b8d4)"></div><p>Lavender Rose</p></div>
<div class="item" style="left:503px"><div class="pic" role="img" aria-label="Girl in beige dress and knit hat" style="background:linear-gradient(#f7f4f0,#d7bba4)"></div><p>Lavender Rose</p></div>
<div class="item" style="left:624px"><div class="pic" role="img" aria-label="Girl in white floral dress" style="background:linear-gradient(#ffffff,#e9d6dc)"></div><p>Lavender Rose</p></div>
<div class="item" style="left:746px"><div class="pic" role="img" aria-label="Girl in light blue top" style="background:linear-gradient(#e4e8ea,#7cc7e4)"></div><p>Lavender Rose</p></div>

<footer class="abs footer"></footer>
<div class="abs foot-brand">Trocadim</div>
<div class="abs foot-contact">
  ola@trocadim.com<br>
  <span>T:</span>+55 11 2345 6789<br>
  <span>M:</span>+55 11 900 000 000
</div>
<div class="abs foot-col" style="left:318px">SHOPPING WITH US
  <ul><li>Ordering &amp; Payment</li><li>Delivery Information</li><li>Returns &amp; Refunds</li></ul>
</div>
<div class="abs foot-col" style="left:506px">HELP
  <ul><li>FAQs</li><li>Contact Us</li><li>Forgot Login Details?</li></ul>
</div>
<div class="abs foot-col" style="left:686px">SOCIAL MEDIA</div>
<div class="abs social">
  <i role="img" aria-label="tweeplr" style="background:#4fc1ea"></i>
  <i role="img" aria-label="chatterbook" style="background:#2d4f8f"></i>
  <i role="img" aria-label="k+" style="background:#3a8fd8"></i>
  <i role="img" aria-label="boardlyx" style="background:#d6282c"></i>
</div>
<div class="abs cards" role="img" aria-label="Accepted payment cards">
  <i style="background:#2a3f8f"></i><i style="background:#1f4fa0"></i><i style="background:#e8463a"></i><i style="background:#2a7fcf"></i><i style="background:#20366f"></i>
</div>

</body>
</html>
```